Exciting new vermouth brand needs a brilliant label!

We need a label design for an exciting new premium Italian Vermouth brand called Brunavera Vermouth.

Brunavera Vermouth is based on a recipe that has been handed down for four generations and is made in the traditional way in the Piedmonte region of Northern Italy.

Brunavera, which means 'heavenly' in Italian has been designed to elevate classic cocktails such as the Negroni, Americano and Manhattan with a base of Italian wine blended with botanicals such as wormwood, orange peel, rhubarb and cinchona. It has a delicately balanced bittersweet profile with hints of vanilla and citrus.

Its competitors include brands such as Vecchia Torre, Parelli and Danvelo (see the uploaded brief for more examples).

The label is for a 50cl dark bottle (please refer to the uploaded brief) and should be based on maximum dimensions of 70mm (width) x 110mm (height). There is no limit to embellishments such as foil printing, embossing or any other premium finishes. The label does not necessarily need to be rectangular.

Feedback will be given quickly and constructively after submissions to ensure that the process is as fair and useful as possible for everyone.

Target Market(s)

25-45 year old Europeans, 50:50 female:male

Industry/Entity Type

Wine / Spirits / Vermouth

Requirements
Must have
• Fantastic design that is distinct from competitors, a premium feel and great lettering.
Should not have
• Generic images or patterns that do not relate to the brand (Brunavera) or the product

```html
<!DOCTYPE html>
<html lang="it">
<head>
<meta charset="utf-8">
<title>Brunavera Vermouth – Sweet Rosso Label</title>
<link rel="stylesheet" href="https://fonts.googleapis.com/css2?family=Cormorant+Garamond:wght@500;600&family=Josefin+Sans:wght@600;700&family=PT+Sans&display=swap">
<style>
  :root {
    --backdrop: #000000;
    --paper: #ffffff;
    --sky: #a9cdf3;
    --sky-ink: #5b9de3;
    --rosso: #b5062f;
    --gold: #b39a68;
    --gold-dark: #9c8152;
    --ink: #0b0b0b;
  }
  html, body {
    margin: 0;
    padding: 0;
    width: 1200px;
    height: 2556px;
    overflow: hidden;
    background: var(--backdrop);
  }
  .stage {
    width: 1200px;
    height: 2556px;
    display: flex;
    align-items: center;
    justify-content: center;
  }
  .label { width: 1000px; height: 1426px; display: block; }
  .label-edge { fill: var(--paper); }
  .pattern-field { fill: var(--sky); }
  .crest-field { fill: var(--paper); }
  .variety-field { fill: var(--rosso); }
  .variety-rule { stroke: var(--paper); stroke-width: 1.6; }
  .heritage {
    font-family: "Cormorant Garamond", serif;
    font-weight: 500;
    font-size: 25px;
    fill: var(--gold);
    letter-spacing: 0.2px;
  }
  .ribbon-face { fill: var(--gold); }
  .ribbon-fold { fill: var(--gold-dark); }
  .ribbon-word {
    font-family: "PT Sans", sans-serif;
    font-size: 38px;
    fill: var(--paper);
  }
  .originale {
    font-family: "Cormorant Garamond", serif;
    font-weight: 600;
    font-size: 19px;
    fill: var(--ink);
    letter-spacing: 0.5px;
  }
  .originale-rule { stroke: var(--ink); stroke-width: 1.2; }
  .brand-name {
    font-family: "Josefin Sans", sans-serif;
    font-weight: 700;
    font-size: 92px;
    fill: var(--ink);
  }
  .variety-name {
    font-family: "Josefin Sans", sans-serif;
    font-weight: 600;
    font-size: 48px;
    fill: var(--paper);
    letter-spacing: 1px;
  }
  .serving {
    font-family: "PT Sans", sans-serif;
    font-size: 40px;
    fill: var(--sky-ink);
  }
  .volume {
    font-family: "PT Sans", sans-serif;
    font-size: 24px;
    fill: var(--ink);
  }
</style>
</head>
<body>
<main class="stage">
  <svg class="label" viewBox="0 0 645 920" xmlns="http://www.w3.org/2000/svg">
    <defs>
      <radialGradient id="flourish-tone" cx="50%" cy="50%" r="50%">
        <stop offset="0%" stop-color="#b39a68" stop-opacity="0.55"/>
        <stop offset="100%" stop-color="#b39a68" stop-opacity="0"/>
      </radialGradient>
    </defs>

    <!-- outer hexagonal label shape -->
    <polygon class="label-edge" points="321,0 645,188 645,732 321,920 0,732 0,188"/>

    <!-- blue damask field -->
    <polygon class="pattern-field" role="img" aria-label="Light blue field with blue scrolling damask ornament"
             points="321,22 629,200 629,742 16,742 16,200"/>

    <!-- central white crest triangle -->
    <polygon class="crest-field" points="321,24 628,543 16,543"/>

    <!-- red variety triangle -->
    <polygon class="variety-field" points="16,543 628,543 321,722"/>

    <!-- lower blue damask tip -->
    <polygon class="pattern-field" role="img" aria-label="Light blue field with blue damask ornament"
             points="198,828 448,828 321,900"/>

    <!-- gold flourish -->
    <ellipse cx="323" cy="190" rx="86" ry="46" fill="url(#flourish-tone)" role="img"
             aria-label="Gold calligraphic flourish"/>

    <!-- heritage line -->
    <text class="heritage" x="322" y="278" text-anchor="middle">ANTICA RICETTA</text>
    <text class="heritage" x="322" y="302" text-anchor="middle">DI VERMOUTH PREGIATO</text>

    <!-- ribbon banner -->
    <g class="ribbon">
      <polygon class="ribbon-fold" points="173,423 186,378 214,382 220,418"/>
      <polygon class="ribbon-fold" points="471,423 458,378 430,382 424,418"/>
      <path class="ribbon-face" d="M199,350 Q322,320 445,350 L440,402 Q322,374 204,402 Z"/>
      <polygon class="ribbon-fold" points="204,402 214,382 186,378 175,420 220,418"/>
      <polygon class="ribbon-fold" points="440,402 430,382 458,378 469,420 424,418"/>
      <path id="ribbon-arc" d="M214,385 Q322,352 430,385" fill="none"/>
      <text class="ribbon-word" text-anchor="middle">
        <textPath href="#ribbon-arc" startOffset="50%">VERMOUTH</textPath>
      </text>
    </g>

    <!-- originale -->
    <line class="originale-rule" x1="258" y1="399" x2="384" y2="399"/>
    <text class="originale" x="321" y="418" text-anchor="middle">ORIGINALE</text>
    <line class="originale-rule" x1="258" y1="423" x2="384" y2="423"/>

    <!-- brand name -->
    <text class="brand-name" x="321" y="512" text-anchor="middle" textLength="457" lengthAdjust="spacingAndGlyphs">BRUNAVERA</text>

    <!-- variety -->
    <text class="variety-name" x="321" y="604" text-anchor="middle">SWEET ROSSO</text>
    <g class="variety-rules">
      <line class="variety-rule" x1="181" y1="628" x2="461" y2="628"/>
      <line class="variety-rule" x1="196" y1="638" x2="446" y2="638"/>
      <line class="variety-rule" x1="212" y1="648" x2="430" y2="648"/>
      <line class="variety-rule" x1="229" y1="658" x2="413" y2="658"/>
      <line class="variety-rule" x1="246" y1="668" x2="396" y2="668"/>
      <line class="variety-rule" x1="264" y1="678" x2="378" y2="678"/>
      <line class="variety-rule" x1="281" y1="688" x2="361" y2="688"/>
    </g>

    <!-- serving and volume -->
    <text class="serving" x="322" y="789" text-anchor="middle">SERVED CHILLED</text>
    <text class="volume" x="322" y="817" text-anchor="middle">750 ml</text>
  </svg>
</main>
</body>
</html>
```